Outdoor sign for Brightwater Auto Restoration

I need a horizontal 4'x 8' outdoor roadside sign for my classic auto restoration business. I have uploaded colors and our logo. Needs the Brightwater name, a prominent Classic AUTO RESTORATION, phone number and website. We rebuild and restore vintage cars, trucks and 4x4s. I'd like something clean but possibly retro. Classic Auto Restoration is more important than the Brightwater name. It needs to be visible and readable from the street. NO CLIP ART

Target Market(s)

Customers who need their vintage care restored or upgraded. Men and women ages 25-75

Industry/Entity Type

Automotive

Colors
FFC000
F8CF3A
FAE287
FDF2CF
FEFAEE

Requirements
Must have
• Legible. Bright. Readable as a backlit 4' x 8' large horizontal sign (roughly 120cm X 240cm)
Nice to have
• Use of the Brightwater logo/type, Complete or Classic before prominent AUTO RESTORATION
Should not have
• Clip art of old cars or icons. And we don't want the Brightwater Logo from the website because it wont be legible from the road. I have included the Illustrator file for Brightwater text in the uploads

```html
<!DOCTYPE html>
<html lang="en">
<head>
<meta charset="utf-8">
<title>Brightwater Auto Restoration – Roadside Sign</title>
<link href="https://fonts.googleapis.com/css2?family=Big+Shoulders+Display:wght@700;800;900&family=Oswald:wght@700&family=Poppins:wght@600;700&display=swap" rel="stylesheet">
<style>
  :root {
    --backdrop: #878787;
    --sign-border: #f4f3ef;
    --panel-dark: #1e1c1d;
    --panel-mid: #3a3839;
    --gold: #f2b01e;
    --gold-deep: #e8a412;
    --white: #ffffff;
    --red: #c8200e;
    --red-deep: #a81808;
    --photo-red: #d3242a;
    --photo-dark: #5a1014;
  }
  * { margin: 0; padding: 0; box-sizing: border-box; }
  html, body { width: 840px; height: 1200px; overflow: hidden; }
  body { background: var(--backdrop); position: relative; font-family: "Poppins", sans-serif; }

  .sign {
    position: absolute; left: 20px; top: 400px;
    width: 800px; height: 400px;
    background: var(--sign-border);
    box-shadow: 0 6px 18px rgba(0,0,0,0.35);
  }
  .sign-panel {
    position: absolute; left: 10px; top: 9px; right: 10px; bottom: 9px;
    border-radius: 12px; overflow: hidden;
    background: radial-gradient(ellipse at 72% 62%, var(--panel-mid) 0%, var(--panel-dark) 62%);
  }
  .sun-disc { position: absolute; left: 0; top: 0; width: 780px; height: 382px; }
  .car-photo {
    position: absolute; left: 466px; top: 44px; width: 307px; height: 177px;
    border-radius: 40px 40px 30px 30px;
    background: radial-gradient(ellipse at 50% 45%, var(--photo-red) 0%, #b51b20 55%, var(--photo-dark) 100%);
  }

  .headline { position: absolute; left: 32px; font-family: "Big Shoulders Display", sans-serif; font-weight: 800; line-height: 1; text-transform: uppercase; white-space: nowrap; }
  .headline-classic { top: 34px; font-size: 84px; color: var(--gold); letter-spacing: -1px; }
  .headline-restoration { top: 108px; font-size: 90px; color: var(--white); letter-spacing: 0.5px; text-shadow: 2px 2px 0 var(--gold-deep); }

  .services-title { position: absolute; left: 31px; top: 207px; font-weight: 700; font-size: 28px; color: var(--white); letter-spacing: 0.3px; white-space: nowrap; }
  .service-list { position: absolute; left: 31px; top: 248px; display: flex; gap: 18px; list-style: none; }
  .service { display: flex; align-items: flex-start; gap: 6px; color: var(--white); font-weight: 600; font-size: 18.5px; line-height: 1.15; white-space: nowrap; }
  .service svg { width: 16px; height: 16px; margin-top: 4px; flex: none; }

  .phone-band {
    position: absolute; left: -10px; top: 315px; width: 304px; height: 48px;
    background: linear-gradient(90deg, var(--red-deep), var(--red));
    border-radius: 0 24px 24px 0;
    display: flex; align-items: center; padding-left: 44px; gap: 8px;
  }
  .phone-band svg { width: 20px; height: 20px; flex: none; }
  .phone-number { font-family: "Big Shoulders Display", sans-serif; font-weight: 800; font-size: 42px; color: var(--white); line-height: 1; white-space: nowrap; }

  .website { position: absolute; left: 313px; top: 321px; display: flex; align-items: center; gap: 8px; }
  .website svg { width: 20px; height: 20px; flex: none; }
  .website-address { font-family: "Big Shoulders Display", sans-serif; font-weight: 700; font-size: 35px; color: var(--white); letter-spacing: 1.5px; text-transform: uppercase; line-height: 1; white-space: nowrap; }

  .business-name { position: absolute; left: 480px; top: 252px; width: 300px; text-align: center; font-family: "Oswald", sans-serif; font-weight: 700; font-size: 42px; color: var(--gold); text-transform: uppercase; line-height: 1; white-space: nowrap; }
</style>
</head>
<body>
  <section class="sign">
    <div class="sign-panel">
      <svg class="sun-disc" viewBox="0 0 780 382" aria-hidden="true">
        <circle cx="626" cy="118" r="146" fill="var(--gold)"/>
      </svg>
      <div class="car-photo" role="img" aria-label="Photo of a restored red vintage sports car, front view"></div>

      <h1 class="headline headline-classic">Classic Auto</h1>
      <h1 class="headline headline-restoration">Restoration</h1>

      <p class="services-title">REBUILD , RESTORE &amp; REPAIR</p>
      <ul class="service-list">
        <li class="service"><svg viewBox="0 0 16 16"><circle cx="8" cy="8" r="6.8" fill="none" stroke="var(--gold)" stroke-width="1.4"/><path d="M4.8 8.2l2.2 2.2 4.2-4.4" fill="none" stroke="var(--gold)" stroke-width="1.5"/></svg><span>Vintage American<br>made car</span></li>
        <li class="service"><svg viewBox="0 0 16 16"><circle cx="8" cy="8" r="6.8" fill="none" stroke="var(--gold)" stroke-width="1.4"/><path d="M4.8 8.2l2.2 2.2 4.2-4.4" fill="none" stroke="var(--gold)" stroke-width="1.5"/></svg><span>Trucks</span></li>
        <li class="service"><svg viewBox="0 0 16 16"><circle cx="8" cy="8" r="6.8" fill="none" stroke="var(--gold)" stroke-width="1.4"/><path d="M4.8 8.2l2.2 2.2 4.2-4.4" fill="none" stroke="var(--gold)" stroke-width="1.5"/></svg><span>4x4s</span></li>
      </ul>

      <div class="business-name">Brightwater</div>

      <div class="phone-band">
        <svg viewBox="0 0 24 24" aria-hidden="true"><path d="M6.6 10.8a15 15 0 006.6 6.6l2.2-2.2c.3-.3.7-.4 1-.2 1.1.4 2.3.6 3.6.6.6 0 1 .4 1 1V20c0 .6-.4 1-1 1A17 17 0 013 4c0-.6.4-1 1-1h3.5c.6 0 1 .4 1 1 0 1.3.2 2.5.6 3.6.1.3 0 .7-.2 1z" fill="var(--gold)"/></svg>
        <span class="phone-number">501-555-0147</span>
      </div>

      <div class="website">
        <svg viewBox="0 0 20 20" aria-hidden="true"><circle cx="10" cy="10" r="8.5" fill="none" stroke="var(--gold)" stroke-width="1.6"/><ellipse cx="10" cy="10" rx="3.8" ry="8.5" fill="none" stroke="var(--gold)" stroke-width="1.3"/><path d="M1.5 10h17M3 5.5h14M3 14.5h14" stroke="var(--gold)" stroke-width="1.2"/></svg>
        <span class="website-address">brightwaterautoworks.com</span>
      </div>
    </div>
  </section>
</body>
</html>
```